Physcial Activity & Parkinson's Disease Severity

We are very happy with the with the infographic below (on diet and PD progression). Now, we need a new infographic on the relationship between physical activity and PD progression.

Target Market(s)

Individuals with parkinonsonism (35-100 y), both genders, as well as their physicians, family members, support group leaders, etc.

Industry/Entity Type

Medicine

Requirements
Must have
• The same information as is listed in the top left corner of the previous infographic on Diet. (For more information: www.brightstepwellnessforall.com, For study info: www.TRVStudyQN.Holmecrest.edu), 2020, RT Vandorne, etc.
Nice to have
• It should fit in nicely with the other ones from a design standpoint.

```html
<!DOCTYPE html>
<html lang="en">
<head>
<meta charset="utf-8">
<title>Physical Activity &amp; Parkinson's Disease Severity</title>
<link rel="stylesheet" href="https://fonts.googleapis.com/css2?family=Source+Sans+3:ital,wght@0,400;0,600;1,400&family=Source+Serif+4:wght@400;700&display=swap">
<style>
  :root {
    --page: #f7f7f7;
    --crimson: #a0252a;
    --crimson-dark: #8f2225;
    --band-grey: #dfdee3;
    --axis-grey: #d9dadf;
    --frame-grey: #d6d6dc;
    --ink: #1e1e1e;
    --black: #000;
    --white: #fff;
    --green: #4a7f3e;
    --green-light: #8db84a;
    --green-dark: #2e5e34;
    --poor: #a3282b;
    --fair: #dc7a5c;
    --good: #c5d488;
    --good-text: #eef2d6;
    --excellent: #8db858;
    --serif: "Source Serif 4", Georgia, serif;
    --sans: "Source Sans 3", Arial, sans-serif;
  }
  html, body { margin: 0; padding: 0; }
  body {
    width: 1200px; height: 1169px; overflow: hidden;
    background: var(--page); position: relative;
    font-family: var(--sans); color: var(--ink);
  }
  .header-shape { position: absolute; left: 0; top: 0; width: 1200px; height: 258px; }
  .header-shape .grey { fill: var(--band-grey); }
  .header-shape .red { fill: var(--crimson); }
  .year {
    position: absolute; left: 1074px; top: 22px; margin: 0;
    font: 700 43px/1 var(--serif); color: var(--crimson);
  }
  .study-title {
    position: absolute; left: 92px; top: 50px; margin: 0;
    font: 700 43px/47px var(--serif); color: var(--white);
  }
  .authors {
    position: absolute; left: 92px; top: 192px; margin: 0;
    font: italic 400 25px/1 var(--sans); color: var(--white);
  }
  .divider-dots { position: absolute; left: 566px; top: 124px; width: 8px; }
  .divider-dots span { display: block; width: 8px; height: 8px; border-radius: 50%; background: var(--white); margin-bottom: 9px; }
  .links { position: absolute; left: 648px; top: 70px; margin: 0; color: var(--white); }
  .links dt { font: italic 400 23px/1 var(--sans); margin: 0; }
  .links dd { font: 700 21px/1 var(--serif); letter-spacing: 0.5px; margin: 8px 0 39px; }

  .chart { position: absolute; overflow: visible; }
  .chart text { font-family: var(--sans); }
  .chart .title { font-family: var(--serif); font-size: 36px; fill: var(--ink); text-anchor: middle; }
  .chart .tick { font-size: 20px; fill: var(--ink); }
  .chart .tick-lg { font-size: 28px; fill: var(--ink); }
  .chart .axis-label { font-size: 30px; font-style: italic; fill: var(--ink); text-anchor: middle; }
  .chart .rail { fill: var(--black); }
  .chart .rail-label { font-size: 38px; font-style: italic; fill: var(--white); text-anchor: middle; }
  .chart .rail-tick { font-size: 18px; fill: var(--white); text-anchor: middle; }
  .chart .axis-band { fill: var(--axis-grey); }
  .chart .arrow { stroke: var(--ink); stroke-width: 2.5; fill: none; }
  .chart .arrow-head { fill: var(--ink); }
  .chart .frame { fill: none; stroke: var(--frame-grey); stroke-width: 4; }
  .series-overweight { fill: none; stroke: var(--green); stroke-width: 4; stroke-linejoin: round; }
  .series-normal { fill: none; stroke: var(--crimson-dark); stroke-width: 4; stroke-linejoin: round; }
  .pill-green { fill: var(--green); }
  .pill-red { fill: var(--crimson-dark); }
  .pill-text { font-size: 28px; font-style: italic; fill: var(--white); text-anchor: middle; }
  .band-poor { fill: var(--poor); }
  .band-fair { fill: var(--fair); }
  .band-good { fill: var(--good); }
  .band-excellent { fill: var(--excellent); }
  .band-label { font-size: 42px; fill: var(--white); text-anchor: end; }
  .band-label.on-good { fill: var(--good-text); }
  .trend { stroke: var(--white); stroke-width: 4; }
  .trend-dot { fill: var(--white); }
  .bar-label { font-size: 25px; font-style: italic; fill: var(--ink); }
  .value { font-size: 18px; fill: var(--ink); text-anchor: middle; }
  .impact-title { font-size: 36px; font-style: italic; fill: var(--ink); text-anchor: middle; }
</style>
</head>
<body>

<header>
  <svg class="header-shape" viewBox="0 0 1955 420" aria-hidden="true">
    <rect class="grey" x="38" y="30" width="1882" height="90"/>
    <path class="red" d="M38,62 H1650 C1705,62 1715,120 1775,120 H1920 V408 H38 Z"/>
  </svg>
  <p class="year">2020</p>
  <h1 class="study-title">Physcial Activity &amp;<br>Parkinson's Disease<br>Severity</h1>
  <p class="authors">RT Vandorne et al.</p>
  <div class="divider-dots"><span></span><span></span><span></span></div>
  <dl class="links">
    <dt>For study details:</dt>
    <dd>www.BrightStepWellnessForAll.com</dd>
    <dt>To participate in this study:</dt>
    <dd>www.TRVStudyQN.Holmecrest.edu</dd>
  </dl>
</header>

<main>
  <!-- Symptom severity by weight -->
  <svg class="chart" style="left:23px;top:270px;width:569px;height:430px" viewBox="38 440 927 700" role="img" aria-label="Line chart: overweight individuals reported greater symptom severity">
    <text class="title" x="537" y="478">Overweight Individuals Reported</text>
    <text class="title" x="537" y="515">Greater Symptom Severity</text>
    <rect class="rail" x="38" y="530" width="55" height="527"/>
    <text class="rail-label" transform="translate(78 800) rotate(-90)">PRO-PD</text>
    <g class="tick">
      <text x="103" y="587">1400</text><text x="103" y="662">1200</text>
      <text x="103" y="736">1000</text><text x="112" y="812">800</text>
      <text x="112" y="884">600</text><text x="112" y="959">400</text>
      <text x="112" y="1033">200</text>
    </g>
    <polyline class="series-overweight" points="163,830 238,802 310,817 386,831 460,790 535,797 610,727 686,788 760,722 835,690 908,658"/>
    <polyline class="series-normal" points="163,883 236,890 308,879 386,847 460,874 535,816 610,790 684,766 760,789 835,768 908,732"/>
    <rect class="pill-green" x="268" y="726" width="182" height="38" rx="19"/>
    <text class="pill-text" x="359" y="754">Overweight</text>
    <rect class="pill-red" x="549" y="863" width="228" height="41" rx="20"/>
    <text class="pill-text" x="663" y="892">Not Overweight</text>
    <rect class="axis-band" x="38" y="1070" width="927" height="70"/>
    <g class="tick" text-anchor="middle" style="font-size:22px">
      <text x="158" y="1098">0</text><text x="235" y="1098">1</text><text x="308" y="1098">2</text>
      <text x="383" y="1098">3</text><text x="460" y="1098">4</text><text x="535" y="1098">5</text>
      <text x="608" y="1098">6</text><text x="684" y="1098">7</text><text x="757" y="1098">8</text>
      <text x="833" y="1098">9</text><text x="907" y="1098">10</text>
    </g>
    <line class="arrow" x1="140" y1="1120" x2="378" y2="1120"/>
    <path class="arrow-head" d="M130,1120 l16,-7 v14 z"/>
    <text class="axis-label" x="512" y="1128" style="font-size:28px">Years Since Diagnosis</text>
    <line class="arrow" x1="650" y1="1120" x2="925" y2="1120"/>
    <path class="arrow-head" d="M935,1120 l-16,-7 v14 z"/>
  </svg>

  <!-- Quality of life vs PRO-PD score -->
  <svg class="chart" style="left:609px;top:270px;width:570px;height:430px" viewBox="992 440 928 700" role="img" aria-label="Chart: correlation between quality of life and PRO-PD score over years since diagnosis">
    <text class="title" x="1494" y="478">Correlation Between Quality of Life and</text>
    <text class="title" x="1494" y="515">PRO-PD Score</text>
    <rect class="rail" x="992" y="530" width="55" height="525"/>
    <text class="rail-label" transform="translate(1033 808) rotate(-90)">PRO-PD SCORE</text>
    <g class="tick-lg" text-anchor="end">
      <text x="1115" y="546">2500</text><text x="1115" y="669">2000</text>
      <text x="1115" y="783">1500</text><text x="1115" y="879">1000</text>
      <text x="1115" y="976">500</text>
    </g>
    <rect class="band-poor" x="1127" y="530" width="724" height="244"/>
    <rect class="band-fair" x="1127" y="774" width="724" height="91"/>
    <rect class="band-good" x="1127" y="865" width="724" height="98"/>
    <rect class="band-excellent" x="1127" y="963" width="724" height="93"/>
    <text class="band-label" x="1820" y="678">Poor</text>
    <text class="band-label" x="1820" y="834">Fair</text>
    <text class="band-label on-good" x="1820" y="933">Good</text>
    <text class="band-label" x="1820" y="1026">Excellent</text>
    <rect class="rail" x="1865" y="530" width="55" height="525"/>
    <text class="rail-label" transform="translate(1906 808) rotate(-90)">Quality of Life</text>
    <line class="trend" x1="1153" y1="940" x2="1760" y2="716"/>
    <g class="trend-dot">
      <circle cx="1202" cy="922" r="12"/><circle cx="1293" cy="888" r="12"/>
      <circle cx="1397" cy="850" r="12"/><circle cx="1501" cy="811" r="12"/>
      <circle cx="1602" cy="773" r="12"/><circle cx="1709" cy="734" r="12"/>
    </g>
    <rect class="axis-band" x="992" y="1070" width="928" height="68"/>
    <g class="tick-lg" text-anchor="middle">
      <text x="1101" y="1101">0</text><text x="1200" y="1101">5</text><text x="1294" y="1101">10</text>
      <text x="1398" y="1101">15</text><text x="1500" y="1101">20</text><text x="1602" y="1101">25</text>
      <text x="1706" y="1101">30</text><text x="1807" y="1101">35</text>
    </g>
    <line class="arrow" x1="1072" y1="1118" x2="1330" y2="1118"/>
    <path class="arrow-head" d="M1062,1118 l16,-7 v14 z"/>
    <text class="axis-label" x="1466" y="1126" style="font-size:28px">Years Since Diagnosis</text>
    <line class="arrow" x1="1600" y1="1118" x2="1845" y2="1118"/>
    <path class="arrow-head" d="M1855,1118 l-16,-7 v14 z"/>
  </svg>

  <!-- Exercise frequency impact -->
  <svg class="chart" style="left:22px;top:716px;width:570px;height:433px" viewBox="36 1166 928 706" role="img" aria-label="Bar chart: PRO-PD impact by exercise frequency">
    <defs>
      <linearGradient id="impactFill" x1="0" y1="0" x2="1" y2="0">
        <stop offset="0" stop-color="#8db84a"/>
        <stop offset="1" stop-color="#2e5e34"/>
      </linearGradient>
    </defs>
    <rect class="frame" x="38" y="1168" width="924" height="702"/>
    <text class="title" x="500" y="1235">Chart Name?</text>
    <g class="bar-label" text-anchor="end">
      <text x="716" y="1320">Exercise 30+ min/d, 7 days/wk</text>
      <text x="716" y="1377">Exercise 30+ min/d, 6 days/wk</text>
      <text x="716" y="1437">Exercise 30+ min/d, 5 days/wk</text>
      <text x="716" y="1495">Exercise 30+ min/d, 4 days/wk</text>
      <text x="716" y="1553">Exercise 30+ min/d, 3 days/wk</text>
      <text x="716" y="1610">Exercise 30+ min/d, 2 days/wk</text>
      <text x="716" y="1670">Exercise 30+ min/d, 1 days/wk</text>
      <text x="716" y="1721">Exercise 30+ min/d, 0 days/wk</text>
    </g>
    <g fill="url(#impactFill)">
      <rect x="283" y="1325" width="435" height="20"/>
      <rect x="296" y="1382" width="422" height="20"/>
      <rect x="375" y="1441" width="343" height="20"/>
      <rect x="385" y="1498" width="333" height="20"/>
      <rect x="439" y="1557" width="279" height="20"/>
    </g>
    <rect x="690" y="1614" width="28" height="20" fill="#2e5e34"/>
    <rect x="632" y="1673" width="86" height="20" fill="#2e5e34"/>
    <rect class="rail" x="102" y="1760" width="795" height="37" rx="18"/>
    <g class="rail-tick">
      <text x="135" y="1785">-400</text><text x="209" y="1785">-350</text><text x="283" y="1785">-300</text>
      <text x="356" y="1785">-250</text><text x="430" y="1785">-200</text><text x="502" y="1785">-150</text>
      <text x="576" y="1785">-100</text><text x="649" y="1785">-50</text><text x="718" y="1785">0</text>
      <text x="793" y="1785">50</text><text x="869" y="1785">100</text>
    </g>
    <rect class="pill-green" x="50" y="1810" width="257" height="42" rx="21"/>
    <text class="pill-text" x="178" y="1840">Better then Average</text>
    <text class="impact-title" x="512" y="1844">PRO-PD Impact</text>
    <rect class="pill-red" x="690" y="1810" width="256" height="42" rx="21"/>
    <text class="pill-text" x="818" y="1840">Worse then Average</text>
  </svg>

  <!-- Activity types -->
  <svg class="chart" style="left:608px;top:716px;width:570px;height:433px" viewBox="992 1166 928 706" role="img" aria-label="Bar chart: PRO-PD impact by type of physical activity and percent reporting participation">
    <defs>
      <linearGradient id="activityFill" gradientUnits="userSpaceOnUse" x1="0" y1="1590" x2="0" y2="1700">
        <stop offset="0" stop-color="#8db84a"/>
        <stop offset="1" stop-color="#2e5e34"/>
      </linearGradient>
    </defs>
    <rect class="frame" x="994" y="1168" width="924" height="702"/>
    <text class="title" x="1456" y="1235">Chart Name?</text>
    <rect class="rail" x="1038" y="1226" width="42" height="616" rx="20"/>
    <g class="rail-tick">
      <text x="1059" y="1267">300</text><text x="1059" y="1346">250</text><text x="1059" y="1420">200</text>
      <text x="1059" y="1499">150</text><text x="1059" y="1579">100</text><text x="1059" y="1657">50</text>
      <text x="1059" y="1735">0</text><text x="1059" y="1812">-50</text>
    </g>
    <g fill="url(#activityFill)">
      <rect x="1137" y="1408" width="35" height="320"/>
      <rect x="1214" y="1559" width="35" height="169"/>
      <rect x="1290" y="1592" width="35" height="136"/>
      <rect x="1367" y="1603" width="35" height="125"/>
      <rect x="1446" y="1615" width="35" height="113"/>
      <rect x="1523" y="1661" width="35" height="67"/>
      <rect x="1600" y="1661" width="35" height="67"/>
      <rect x="1677" y="1678" width="35" height="50"/>
      <rect x="1753" y="1717" width="35" height="11"/>
      <rect x="1831" y="1723" width="35" height="5"/>
    </g>
    <g class="bar-label">
      <text transform="translate(1163 1398) rotate(-90)">Running</text>
      <text transform="translate(1240 1549) rotate(-90)">Other</text>
      <text transform="translate(1316 1582) rotate(-90)">Yoga</text>
      <text transform="translate(1393 1593) rotate(-90)">Hiking</text>
      <text transform="translate(1472 1605) rotate(-90)">Biking</text>
      <text transform="translate(1549 1651) rotate(-90)">Walking</text>
      <text transform="translate(1626 1651) rotate(-90)">Tai Chi</text>
      <text transform="translate(1703 1668) rotate(-90)">Dance</text>
      <text transform="translate(1779 1707) rotate(-90)">Firm Footing Boxing</text>
      <text transform="translate(1857 1713) rotate(-90)">Swimming</text>
    </g>
    <rect class="axis-band" x="1093" y="1745" width="797" height="67"/>
    <g class="value">
      <text x="1154" y="1767">9.9</text><text x="1232" y="1767">46.2</text><text x="1307" y="1767">22.5</text>
      <text x="1385" y="1767">11.9</text><text x="1463" y="1767">25.0</text><text x="1541" y="1767">73.5</text>
      <text x="1618" y="1767">10.0</text><text x="1694" y="1767">11.4</text><text x="1770" y="1767">6.8</text>
      <text x="1848" y="1767">10.6</text>
    </g>
    <line class="arrow" x1="1115" y1="1792" x2="1340" y2="1792"/>
    <path class="arrow-head" d="M1105,1792 l16,-7 v14 z"/>
    <text class="axis-label" x="1493" y="1801">% reporting participation</text>
    <line class="arrow" x1="1645" y1="1792" x2="1870" y2="1792"/>
    <path class="arrow-head" d="M1880,1792 l-16,-7 v14 z"/>
  </svg>
</main>

</body>
</html>
```